Business Card Design Project

Use our current logo. Clean design.

Industry/Entity Type

Business

Requirements
Must have
• Marisela DUBRANCQ
M. Law
Managing Partner

Alpenvorsa AG
Kornhalmweg 214
CH-3097 Liebefeld

M. +41 79 412 56 27
T. +41 31 928 44 10
F. +41 31 928 44 19

m.dubrancq@alpenvorsa-example.com
www.alpenvorsa-example.com

```html
<!DOCTYPE html>
<html lang="en">
<head>
<meta charset="utf-8">
<title>Alpenvorsa AG – Business Card</title>
<link href="https://fonts.googleapis.com/css2?family=Jost:wght@300;400;600&display=swap" rel="stylesheet">
<style>
  :root {
    --paper: #ffffff;
    --sky: #cde3ec;
    --taupe: #8a7b71;
    --ink: #454545;
    --ink-soft: #555555;
    --brand-grey: #7a7a7a;
    --rule: #3f3f3f;
    --on-taupe: #ffffff;
  }
  * { margin: 0; padding: 0; box-sizing: border-box; }
  html, body {
    width: 1200px; height: 686px; overflow: hidden;
    background: var(--paper);
  }
  .card {
    position: relative; width: 1200px; height: 686px; overflow: hidden;
    background: var(--paper);
    font-family: "Jost", "Futura", sans-serif;
    color: var(--ink);
  }
  .card__shapes { position: absolute; inset: 0; }
  .brand {
    position: absolute; left: 16px; top: 248px; width: 320px;
    font-weight: 300; font-size: 41px; letter-spacing: 1.5px;
    color: var(--brand-grey); text-align: center; line-height: 1;
  }
  .holder {
    position: absolute; left: 314px; top: 278px; width: 400px;
    text-align: center; font-weight: 600; line-height: 1;
    letter-spacing: 4px;
  }
  .holder__first { display: block; font-size: 52px; }
  .holder__last { display: block; font-size: 54px; margin-top: 8px; }
  .role {
    position: absolute; left: 248px; top: 466px; width: 212px;
    text-align: center; color: var(--on-taupe);
    font-weight: 400; font-size: 18px; letter-spacing: 1px; line-height: 29px;
  }
  .contact { position: absolute; left: 871px; width: 238px; }
  .contact__rule { border-top: 1.5px solid var(--rule); }
  .address { top: 171px; }
  .address p {
    font-size: 21px; font-weight: 400; letter-spacing: 1.2px;
    line-height: 30.5px; margin-top: 15px;
  }
  .address p span { display: block; }
  .phones { top: 355px; }
  .phones ul { list-style: none; margin-top: 16px; }
  .phones li {
    font-size: 16px; letter-spacing: 1.3px; line-height: 31px; color: var(--ink-soft);
  }
  .phones .label { display: inline-block; width: 28px; }
  .web { top: 538px; }
  .web ul { list-style: none; margin-top: 36px; }
  .web li {
    font-size: 13px; letter-spacing: 0.4px; line-height: 31px; color: var(--ink-soft);
    white-space: nowrap;
  }
</style>
</head>
<body>
<main class="card">
  <svg class="card__shapes" width="1200" height="686" viewBox="0 0 1200 686" aria-hidden="true">
    <circle class="shape-sky" cx="189" cy="189" r="243" fill="var(--sky)"/>
    <circle class="shape-taupe" cx="354" cy="494" r="106" fill="var(--taupe)"/>
  </svg>

  <div class="brand">ALPENVORSA</div>

  <h1 class="holder">
    <span class="holder__first">Marisela</span>
    <span class="holder__last">DUBRANCQ</span>
  </h1>

  <p class="role">M. Law<br>Managing Partner</p>

  <section class="contact address">
    <div class="contact__rule"></div>
    <p>
      <span>Alpenvorsa AG</span>
      <span>Kornhalmweg 214</span>
      <span>CH-3097 Liebefeld</span>
    </p>
  </section>

  <section class="contact phones">
    <div class="contact__rule"></div>
    <ul>
      <li><span class="label">M.</span>+41 79 412 56 27</li>
      <li><span class="label">T.</span>+41 31 928 44 10</li>
      <li><span class="label">F.</span>+41 31 928 44 19</li>
    </ul>
  </section>

  <section class="contact web">
    <div class="contact__rule"></div>
    <ul>
      <li>m.dubrancq@alpenvorsa-example.com</li>
      <li>www.alpenvorsa-example.com</li>
    </ul>
  </section>
</main>
</body>
</html>
```